New Template, new corporate image Quelmoro 2022

New template designs for google slides or PowerPoint. Match to new corporate image. The new website www.quelmoro-mx.com Needs to match our new version. Technology and Artificial Intelligence elements to reflect our type of work.
We are adding old version of template and will send elements for the new corporate images.
Please consider our website as the main corporate image.
Our templates are being used on customer presentations, webminars, internal work only.
We have our main name of company Quelmoro. Quelmoro has to be in all the templates.
Secondary logo or branded service is: Calvindar.

Target Market(s)

Industrial users. Asset managers. Corporate visitors and customers.

Industry/Entity Type

Automotive. Chemical. Food and Beverage. Manufacturing

Other font styles liked:
• GE INSPIRA. RALEWAY

Colors
0054AA
0677BA
7BADD7
CADEEF
E8F1F8

Requirements
Must have
• Match to our elements on the new image. Use Brain Icons. Chips icons to connect equipments with software and control. Innovation.
Nice to have
• Unique images, machine images. Connecting machines and data elements. Template version for google slides. Image for industrial software for control equipment and saving money to manufacturers. Segments: Automotive, Chemical, Food and Beverages, Mining and pharmaceutical, Energy Management
Should not have
• old elements. not to much images of medical devices. Do not seems like a hospital.

```html
<!DOCTYPE html>
<html lang="en">
<head>
<meta charset="utf-8">
<title>Quelmoro 2022 Slide Template</title>
<link rel="stylesheet" href="https://fonts.googleapis.com/css2?family=Barlow+Semi+Condensed:wght@500;600&family=Nunito+Sans:wght@400;600;700&family=Raleway:wght@500&display=swap">
<style>
:root{
  --blue-deep:#0054AA;
  --blue:#1673BD;
  --blue-mid:#0677BA;
  --blue-soft:#7BADD7;
  --blue-pale:#CADEEF;
  --blue-mist:#EEF4FB;
  --ink:#1a1a1a;
  --grey:#555;
  --white:#fff;
}
*{box-sizing:border-box;margin:0;padding:0}
html,body{width:978px;height:1200px;overflow:hidden;background:var(--white)}
body{position:relative;font-family:"Nunito Sans",sans-serif;color:var(--ink)}
.slide{position:absolute;width:408px;height:229px;background:var(--white);overflow:hidden;box-shadow:0 6px 10px rgba(0,0,0,.18)}
.col-l{left:63px}.col-r{left:507px}
.row-1{top:65px}.row-2{top:345px}.row-3{top:625px}.row-4{top:905px}
.abs{position:absolute}
.title{position:absolute;left:25px;top:10px;font-family:"Barlow Semi Condensed",sans-serif;font-weight:600;font-size:19px;letter-spacing:.2px;color:var(--ink);white-space:nowrap}
.brand{position:absolute;right:20px;top:13px;font-family:"Raleway",sans-serif;font-weight:500;font-size:10px;color:var(--blue);display:flex;align-items:center;gap:3px}
.brand i{display:block;width:5px;height:5px;background:var(--blue)}
.footer{position:absolute;left:0;right:0;bottom:0;height:12px;background:var(--blue)}
.footer span{position:absolute;left:26px;top:3px;font-size:3.8px;color:var(--white)}
.stage{position:absolute;left:0;right:0;top:38px;bottom:12px;background:var(--blue-mist)}
.photo{position:absolute}
.body-text{font-size:7.4px;line-height:1.25}
.heading-s{font-family:"Barlow Semi Condensed",sans-serif;font-weight:600}
ul.bullets{list-style:none}
ul.bullets li{position:relative;padding-left:10px}
ul.bullets li::before{content:"•";position:absolute;left:0}
/* cover */
.cover{background:linear-gradient(100deg,#05101d 0%,#0a1f38 45%,#0d3560 100%)}
.cover .brand-big{position:absolute;left:21px;top:78px;font-family:"Raleway",sans-serif;font-weight:500;font-size:22px;color:#2f8fe0;display:flex;align-items:center;gap:6px}
.cover .brand-big i{display:block;width:10px;height:10px;background:#2f8fe0}
.cover .tagline{position:absolute;left:22px;top:132px;width:150px;font-size:4.6px;line-height:1.3;color:var(--white)}
/* when to use */
.tab{position:absolute;top:153px;width:57px;height:64px;background:var(--blue)}
.tab p{position:absolute;left:7px;top:25px;width:46px;font-size:3.3px;line-height:1.2;color:var(--white)}
.ring{position:absolute;top:127px;width:52px;height:52px;border-radius:50%;background:var(--white);border:3px solid var(--blue);display:flex;align-items:center;justify-content:center}
/* pills */
.pill{position:absolute;height:19px;width:116px;background:var(--blue);border-radius:2px;color:var(--white);font-size:3.8px;display:flex;align-items:center;padding:0 5px;box-shadow:0 2px 3px rgba(0,0,0,.15)}
.num-bar{position:absolute;left:30px;height:11px;width:90px;background:#2a7fd0;border-radius:2px}
.num-dot{position:absolute;left:-2px;top:-1.5px;width:14px;height:14px;border-radius:50%;background:#2a7fd0;border:1.5px solid var(--white);color:var(--white);font-size:6px;display:flex;align-items:center;justify-content:center}
.panel-blue{position:absolute;left:0;top:38px;width:203px;bottom:12px;background:var(--blue)}
table.grid{position:absolute;left:67px;top:72px;width:271px;border-collapse:collapse;box-shadow:0 3px 6px rgba(0,0,0,.12)}
table.grid td,table.grid th{height:12.4px;border:1px solid var(--white);font-size:4px;color:var(--grey);text-align:center;background:var(--blue-pale)}
table.grid tr:nth-child(even) td{background:#dde9f5}
table.grid th{background:#5b97d3;height:11px}
</style>
</head>
<body>

<!-- Slide 1: cover -->
<section class="slide cover col-l row-1">
  <div class="photo" role="img" aria-label="Glowing blue brain above a circuit board chip" style="left:160px;top:0;width:248px;height:229px;background:radial-gradient(ellipse 45% 35% at 55% 38%,rgba(60,170,255,.55),rgba(10,50,100,.2) 70%,transparent)"></div>
  <div class="brand-big"><i></i>Quelmoro</div>
  <p class="tagline">We are specialists in automation, process control, information technologies, development and consulting for quality, efficiency and production.</p>
</section>

<!-- Slide 2: when to use -->
<section class="slide col-r row-1">
  <h2 class="title" style="left:31px;top:13px">When to use a digital</h2>
  <div class="brand">Quelmoro</div>
  <p class="abs body-text" style="left:31px;top:76px;width:130px;color:var(--grey);font-size:7px">When production assets have a high maintenance cost.</p>
  <div class="tab" style="left:22px"><p>•When a plant has multiple brands of PLC, PAC and controllers for production.</p></div>
  <div class="tab" style="left:84px"><p>•When production assets have a high maintenance cost.</p></div>
  <div class="tab" style="left:146px"><p>•In multiple industrial automation platforms, which require a unified command</p></div>
  <div class="ring" style="left:24px"><svg width="18" height="18" viewBox="0 0 18 18" fill="none" stroke="#1673BD" stroke-width="1.2"><circle cx="9" cy="9" r="7"/><path d="M4 6c2 0 3 1 3 3s2 2 2 4M11 3c0 2 1 3 3 3"/></svg></div>
  <div class="ring" style="left:86px"><svg width="18" height="18" viewBox="0 0 18 18" fill="none" stroke="#1673BD" stroke-width="1.2"><path d="M9 2l6 3v8l-6 3-6-3V5z M3 5l6 3 6-3M9 8v8"/></svg></div>
  <div class="ring" style="left:148px"><svg width="18" height="18" viewBox="0 0 18 18" fill="none" stroke="#1673BD" stroke-width="1.2"><rect x="4" y="4" width="10" height="10"/><rect x="7" y="7" width="4" height="4"/><path d="M6 2v2M9 2v2M12 2v2M6 14v2M9 14v2M12 14v2M2 6h2M2 9h2M2 12h2M14 6h2M14 9h2M14 12h2"/></svg></div>
  <div class="photo" role="img" aria-label="Flying white humanoid robot" style="left:238px;top:70px;width:134px;height:112px;background:radial-gradient(ellipse at center,#c9cde0,#fff 70%)"></div>
  <div class="footer"><span>www.quelmoro-mx.com</span></div>
</section>

<!-- Slide 3 -->
<section class="slide col-l row-2">
  <h2 class="title">Digital Operations Centerc</h2>
  <div class="brand">Quelmoro</div>
  <div class="photo" role="img" aria-label="Engineer in hard hat using an industrial control dashboard" style="left:0;top:38px;width:203px;height:179px;background:linear-gradient(110deg,#1e2a36,#3a4450 45%,#6a5030 75%,#2e3b4a)"></div>
  <div class="photo" role="img" aria-label="Robotic arms in a factory with blue overlay" style="left:203px;top:38px;width:205px;height:179px;background:linear-gradient(160deg,#2f5d88,#3f6f98 50%,#5a6f74)"></div>
  <p class="abs body-text" style="left:29px;top:76px;width:160px;color:var(--white)">For complex production systems that require autonomy, control of PLC equipment, PAC, plants.</p>
  <p class="abs heading-s" style="left:29px;top:126px;font-size:7.5px;color:var(--white)">Digital Operations Center</p>
  <div class="num-bar" style="top:153px"><span class="num-dot">1</span></div>
  <div class="num-bar" style="top:171px"><span class="num-dot">2</span></div>
  <div class="num-bar" style="top:188px"><span class="num-dot">3</span></div>
  <p class="abs heading-s" style="left:228px;top:96px;font-size:11.5px;color:var(--white)">Digital Operations Center</p>
  <p class="abs body-text" style="left:228px;top:126px;width:160px;color:var(--white)">For complex production systems that require autonomy, control of PLC equipment, PAC, Networks, actuators and distributed control systems, a digital command center is the best alternative to continue operating production plants.</p>
  <div class="footer"><span>www.quelmoro-mx.com</span></div>
</section>

<!-- Slide 4 -->
<section class="slide col-r row-2">
  <h2 class="title">Digital Operations Center</h2>
  <div class="brand">Quelmoro</div>
  <div class="stage"></div>
  <div class="pill" style="left:35px;top:89px">There are high security and production risks.</div>
  <div class="pill" style="left:35px;top:114px">There are high security and production risks.</div>
  <div class="pill" style="left:35px;top:141px">There are high security and production risks.</div>
  <div class="pill" style="left:270px;top:89px;width:103px;justify-content:flex-end">There are high security and production risks.</div>
  <div class="pill" style="left:270px;top:114px;width:103px;justify-content:flex-end">There are high security and production risks.</div>
  <div class="pill" style="left:270px;top:141px;width:103px;justify-content:flex-end">There are high security and production risks.</div>
  <svg class="abs" style="left:136px;top:53px" width="144" height="144" viewBox="0 0 144 144">
    <circle cx="72" cy="72" r="71" fill="#fff"/>
    <circle cx="72" cy="72" r="51" fill="none" stroke="#1673BD" stroke-width="15"/>
    <text x="72" y="75" text-anchor="middle" font-family="Raleway, sans-serif" font-size="8" fill="#1673BD">Quelmoro</text>
  </svg>
  <div class="footer"><span>www.quelmoro-mx.com</span></div>
</section>

<!-- Slide 5 -->
<section class="slide col-l row-3">
  <h2 class="title">Digital Operations Center</h2>
  <div class="brand">Quelmoro</div>
  <div class="stage"></div>
  <p class="abs heading-s" style="left:37px;top:78px;font-size:10px">Digital Operations Center</p>
  <ul class="abs bullets body-text" style="left:26px;top:117px;width:150px;font-size:7px">
    <li>For complex production systems that require autonomy, control of PLC equipment, PAC,</li>
    <li>Networks, actuators and distributed control systems, a digital command center is the best alternative to continue operating production plants.</li>
  </ul>
  <div class="photo" role="img" aria-label="Hand holding a tablet with a glowing cloud upload hologram above a city" style="left:203px;top:38px;width:205px;height:179px;background:radial-gradient(ellipse 40% 35% at 50% 40%,#8fb6e8,#26508a 60%,#0d2448)"></div>
  <div class="footer"><span>www.quelmoro-mx.com</span></div>
</section>

<!-- Slide 6 -->
<section class="slide col-r row-3">
  <h2 class="title">Digital Operations Centerc</h2>
  <div class="brand">Quelmoro</div>
  <div class="stage"></div>
  <div class="panel-blue"></div>
  <p class="abs body-text" style="left:23px;top:72px;width:130px;color:var(--white)">When production assets have a high maintenance cost.</p>
  <svg class="abs" style="left:36px;top:138px" width="144" height="52" viewBox="0 0 144 52" fill="#fff">
    <rect x="30" y="0" width="84" height="12" rx="1"/>
    <path d="M72 12v6M22 18h100M22 18v4M72 18v4M122 18v4" stroke="#fff" stroke-width="1" fill="none"/>
    <rect x="0" y="22" width="44" height="12" rx="1"/>
    <rect x="50" y="22" width="44" height="12" rx="1"/>
    <rect x="99" y="22" width="44" height="12" rx="1"/>
    <rect x="0" y="40" width="44" height="12" rx="1"/>
    <rect x="50" y="40" width="44" height="12" rx="1"/>
    <rect x="99" y="40" width="44" height="12" rx="1"/>
  </svg>
  <div class="photo" role="img" aria-label="Small white service robot character" style="left:262px;top:68px;width:86px;height:130px;background:radial-gradient(ellipse at center,#d9dde6,#eef4fb 70%)"></div>
  <div class="footer"><span>www.quelmoro-mx.com</span></div>
</section>

<!-- Slide 7 -->
<section class="slide col-l row-4">
  <h2 class="title">Digital Operations Centerc</h2>
  <div class="brand">Quelmoro</div>
  <div class="stage"></div>
  <div class="panel-blue"></div>
  <svg class="abs" style="left:0;top:38px" width="203" height="179" viewBox="0 0 203 179" fill="none" stroke="#fff" stroke-width="1.3">
    <path d="M61 67H25v67h20M135 67h36v67h-20M72 98v15H45v21M126 98v15h27v21M98 107v27"/>
    <circle cx="98" cy="70" r="37" fill="#fff"/>
    <circle cx="98" cy="70" r="33" stroke="#1673BD"/>
    <text x="98" y="73" text-anchor="middle" font-family="Raleway, sans-serif" font-size="7" fill="#1673BD" stroke="none">Quelmoro</text>
    <g fill="#1673BD" stroke-width="1.5">
      <circle cx="45" cy="136" r="11"/><circle cx="72" cy="136" r="11"/><circle cx="98" cy="136" r="11"/><circle cx="125" cy="136" r="11"/><circle cx="152" cy="136" r="11"/>
    </g>
    <g stroke-width=".9">
      <path d="M40 140l10-8M42 133l8 0v7"/>
      <rect x="68" y="132" width="8" height="7"/><path d="M72 129v3M66 135h2M76 135h2"/>
      <rect x="95" y="130" width="6" height="11"/><path d="M96 133h4"/>
      <circle cx="121" cy="132" r="1.5"/><circle cx="129" cy="132" r="1.5"/><circle cx="125" cy="140" r="1.5"/><path d="M122 133l3 6M128 133l-3 6"/>
      <path d="M154 130l-5 7h4l-2 6 5-8h-4z"/>
    </g>
  </svg>
  <p class="abs heading-s" style="left:223px;top:97px;font-size:7.5px">Digital Operations Center</p>
  <ul class="abs bullets body-text" style="left:215px;top:120px;width:170px;font-size:7px">
    <li>For complex production systems that require autonomy, control of PLC equipment, PAC,</li>
    <li>Networks, actuators and distributed control systems, a digital command center is the best alternative to continue operating production plants.</li>
  </ul>
  <div class="footer"><span>www.quelmoro-mx.com</span></div>
</section>

<!-- Slide 8 -->
<section class="slide col-r row-4">
  <h2 class="title">Digital Operations Centerc</h2>
  <div class="brand">Quelmoro</div>
  <div class="stage"></div>
  <table class="grid">
    <colgroup><col style="width:13px"><col style="width:43px"><col style="width:57px"><col style="width:60px"><col style="width:49px"><col style="width:49px"></colgroup>
    <tr><th></th><th></th><th></th><th></th><th></th><th></th></tr>
    <tr><td>1</td><td></td><td></td><td></td><td></td><td></td></tr>
    <tr><td>2</td><td></td><td></td><td></td><td></td><td></td></tr>
    <tr><td>3</td><td></td><td></td><td></td><td></td><td></td></tr>
    <tr><td>4</td><td></td><td></td><td></td><td></td><td></td></tr>
    <tr><td>5</td><td></td><td></td><td></td><td></td><td></td></tr>
    <tr><td>6</td><td></td><td></td><td></td><td></td><td></td></tr>
    <tr><td>7</td><td></td><td></td><td></td><td></td><td></td></tr>
  </table>
  <div class="footer"><span>www.quelmoro-mx.com</span></div>
</section>

</body>
</html>
```